WP website design (FELM)

We need a wordpress design that will incorporate a professional color scheme with company logo in a clean layout. The design needs to consider that this will be developed on a responsive theme. Colors are undetermined - those that will complement the logo.
Client mentions liking brintonsale.example for the layout and use of color. Possible but not necessary to have large slideshow element.

Industry/Entity Type

It Company

Font styles to use
Sans Serif

Colors

Designer to choose colors to be used in the design.

Requirements
Must have
• - Navigation: 1)Home 2) Auctions 3) Services 4) About Us 5) FAQs 6) References 7) Contact Us

Site will have slideshow, please use high-end stock real estate image initially. Header will have logo. Social icons (Facebook, Twitter, Youtube)

Widgets Include: Email signup form, Featured Auctions, Featured Video widget.

Footer will have contact info (below), site navigation, smaller company logo, affiliation logos (attached).

FELM Auction Group
4172 Quill Ferry Lane
Paducah, KY 42917
1-800-555-BIDS (2437)
Ph. (270) 555-0148
Fx. (270) 555-0193
Nice to have
• - Site will have drop-down menus - please indicate the styling, for instance the dropdown menus 1) Live 2) Online 3) Past - under the 'Auctions' link

```html
<!DOCTYPE html>
<html lang="en">
<head>
<meta charset="utf-8">
<title>FELM Auction Group</title>
<link rel="stylesheet" href="https://fonts.googleapis.com/css2?family=Montserrat:wght@400;600;700&family=Open+Sans:ital,wght@0,400;0,600;0,700;1,400&display=swap">
<style>
:root{
  --red:#e30613;
  --yellow:#ffe400;
  --green:#2e9b1f;
  --ink:#222;
  --grey:#f3f3f3;
  --line:#e9a0a0;
  --white:#fff;
  --nav-dark:#3c3c3c;
}
*{box-sizing:border-box;margin:0;padding:0}
html,body{width:1200px;height:1000px;overflow:hidden;background:var(--white)}
body{position:relative;font-family:"Montserrat",sans-serif;color:var(--ink)}
.abs{position:absolute}
a{color:inherit;text-decoration:none}

/* top bar */
.topbar{left:0;top:0;width:1200px;height:23px;background:var(--red)}
.top-phone{left:142px;top:3px;height:17px;color:var(--white);font-weight:700;font-size:13px;line-height:17px;display:flex;gap:4px;align-items:center;z-index:2}
.search{left:486px;top:3px;width:229px;height:17px;background:#6d0007;border-radius:2px;color:#f2d0d0;font-size:10px;line-height:13px;padding:2px 8px;font-family:"Open Sans",sans-serif}
.search .go{position:absolute;right:0;top:0;width:32px;height:17px;background:#3a3a3a;display:flex;align-items:center;justify-content:center}
.social{left:918px;top:6px;display:flex;gap:3px}
.social span{width:12px;height:12px;background:#ffd2d2;border-radius:1px}

/* header */
.brand{left:142px;top:40px;display:flex;align-items:center;gap:8px;color:var(--red);font-weight:700;font-size:17px;line-height:1}
.brand .dot{width:22px;height:22px;border-radius:50%;background:var(--red)}
.nav{top:56px;font-size:9px;line-height:11px;letter-spacing:.5px;color:#222}
.nav-box{top:53px;height:16px;background:var(--nav-dark);color:var(--white);font-size:9px;line-height:10px;padding:3px 8px;letter-spacing:.5px;border-radius:2px}
.nav-box .caret{position:absolute;right:0;top:0;width:22px;height:16px;background:#555;display:flex;align-items:center;justify-content:center}
.dropdown{left:440px;top:69px;width:143px;z-index:3}
.dropdown li{list-style:none;height:13px;font-size:8.5px;line-height:13px;padding:0 8px;color:var(--white);background:var(--nav-dark);letter-spacing:.5px}
.dropdown li.active{background:var(--red)}

/* hero */
.hero{left:0;top:95px;width:1200px;height:145px;background:linear-gradient(100deg,#f1efe9 0%,#e4dfd6 40%,#dcd6cc 62%,#6ea6d9 80%,#4f8fd0 100%)}

/* featured */
.bar{background:var(--red);color:var(--white)}
.featured-bar{left:140px;top:249px;width:919px;height:19px;font-size:15px;padding:0 18px;line-height:19px}
.card{top:277px;width:206px;text-align:center}
.card .photo{width:206px;height:66px;background:linear-gradient(#b9d3ea,#cfd6c8 55%,#8aa868)}
.card h3{font-size:10.5px;font-weight:600;line-height:10px;margin-top:5px;height:20px}
.card .tag{color:var(--red);font-size:9.5px;font-weight:700;line-height:11px;margin-top:4px;letter-spacing:.3px}
.card .meta{font-family:"Open Sans",sans-serif;font-size:8px;line-height:7.2px;margin-top:4px}
.card .meta + .meta{margin-top:6px}
.card .meta b{font-weight:700;display:block}
.btn{display:inline-block;color:var(--white);font-size:10px;font-weight:600;height:19px;line-height:19px;text-align:center;letter-spacing:.3px}
.btn-red{background:var(--red)}
.btn-green{background:var(--green)}
.card .btn{display:block;width:140px;margin:8px auto 0}
.arrow{top:363px;width:28px;height:14px;background:var(--red);color:var(--white);font-size:10px;text-align:center;line-height:14px}

/* upcoming */
.upcoming{left:140px;top:474px;width:525px;height:466px;background:var(--grey)}
.upcoming-bar{left:140px;top:474px;width:525px;height:18px;font-size:11px;padding:0 18px;line-height:18px}
.item{left:158px;width:490px;height:140px;border-bottom:1px solid var(--line)}
.item .thumb{position:absolute;left:2px;top:0;width:121px;height:59px;background:linear-gradient(135deg,#7e9a6c,#a8b79a 50%,#6c8a5f)}
.item .ribbon{position:absolute;background:#222;color:var(--white);font-size:7px;line-height:9px;padding:1px 6px;transform:rotate(-30deg);transform-origin:left top;top:18px;left:-2px}
.item h4{position:absolute;left:170px;top:-2px;color:var(--red);font-size:10px;line-height:12px;font-weight:700}
.item p{position:absolute;left:170px;top:13px;width:322px;font-size:9.6px;line-height:10.3px}
.item .row{position:absolute;left:0;font-family:"Open Sans",sans-serif;font-size:9.6px;line-height:14px;display:flex;align-items:center;gap:14px}
.item .row b{font-family:"Montserrat",sans-serif;font-weight:700}
.item .row svg{width:14px;height:14px}
.item .actions{position:absolute;top:102px;left:95px;display:flex;gap:37px}
.item .actions .btn{width:132px}
.view-all{left:502px;top:919px;color:var(--red);font-size:11px;line-height:13px;font-weight:600}

/* signup */
.signup{left:684px;top:474px;width:375px;height:243px;background:var(--red);color:var(--white)}
.signup h2{text-align:center;font-size:15px;line-height:14px;margin-top:6px;font-weight:700;letter-spacing:.3px}
.signup h2 em{font-style:normal;color:var(--yellow)}
.signup hr{border:none;border-top:1px solid #f57b7b;margin:9px 0 0}
.signup .sms{font-size:11px;line-height:13px;font-weight:700;margin:6px 0 0 20px}
.signup .num{font-size:14px;line-height:17px;font-weight:700;color:var(--yellow);margin-left:20px}
.signup .or{text-align:center;font-size:11px;line-height:13px;font-weight:700;margin-top:5px}
.signup .lead{font-size:11.3px;font-weight:700;line-height:10.5px;margin:7px 26px 0 20px;letter-spacing:.2px}
.field{position:absolute;left:20px;width:337px;height:18px;background:var(--white);color:#333;font-size:10px;line-height:14px;padding:2px 16px;letter-spacing:.5px}
.send{position:absolute;left:264px;top:214px;width:93px;height:20px;border:1px solid var(--white);text-align:center;font-size:11px;font-weight:700;line-height:18px;letter-spacing:1px}

/* videos */
.video-bar{left:684px;top:727px;width:375px;height:18px;font-size:11px;padding:0 18px;line-height:18px}
.video-bar .nav-arrows{position:absolute;right:12px;top:0;font-size:12px;font-weight:700}
.video{left:703px;top:755px;width:337px;height:96px;background:linear-gradient(90deg,#8a4d3a,#b06a4f 45%,#6f3e30 75%,#c9cbc4)}
.video .play{position:absolute;left:150px;top:38px}
.video-title{left:703px;top:853px;font-size:10.5px;line-height:13px;font-weight:600}
.video-text{left:703px;top:867px;width:340px;font-family:"Open Sans",sans-serif;font-style:italic;font-size:7.5px;line-height:8.4px}
.video-meta{left:703px;top:884px;width:337px;font-family:"Open Sans",sans-serif;font-style:italic;font-size:6.5px;line-height:8px;color:#999}
.video-meta span:last-child{position:absolute;right:0;top:0;display:flex;align-items:center;gap:10px}
.badges{left:710px;top:905px;display:flex;gap:22px;align-items:center}
.badge{background:#222}

/* footer */
.footer{left:0;top:949px;width:1200px;height:37px;background:var(--red)}
.footer-nav{left:140px;top:961px;display:flex;gap:13px;font-size:10px;line-height:12px;color:var(--white)}
.footer-brand{left:730px;top:946px;width:100px;height:42px;border-radius:50%;background:var(--white);color:var(--red);font-size:9px;font-weight:700;display:flex;align-items:center;justify-content:center;text-align:center;line-height:10px}
.footer-contact{left:838px;top:950px;font-family:"Open Sans",sans-serif;font-style:normal;font-size:8.6px;line-height:9px;color:var(--white)}
.footer-contact b{font-weight:700}
.legal{top:987px;font-family:"Open Sans",sans-serif;font-size:8px;line-height:10px;color:var(--red)}
</style>
</head>
<body>

<div class="abs topbar"></div>
<div class="abs top-phone">
  <svg width="14" height="12" viewBox="0 0 24 24"><path fill="#fff" d="M6.6 10.8a15 15 0 0 0 6.6 6.6l2.2-2.2a1 1 0 0 1 1-.3 11 11 0 0 0 3.6.6 1 1 0 0 1 1 1V20a1 1 0 0 1-1 1A17 17 0 0 1 3 4a1 1 0 0 1 1-1h3.5a1 1 0 0 1 1 1c0 1.2.2 2.4.6 3.6a1 1 0 0 1-.3 1z"/></svg>
  1-800-555-BIDS (2437)
</div>
<div class="abs search">Search auctions...
  <span class="go"><svg width="10" height="10" viewBox="0 0 12 12"><circle cx="5" cy="5" r="3.5" stroke="#fff" stroke-width="1.5" fill="none"/><path d="M7.5 7.5L11 11" stroke="#fff" stroke-width="1.5"/></svg></span>
</div>
<div class="abs social"><span></span><span></span><span></span><span></span><span></span><span></span><span></span><span></span><span></span></div>

<div class="abs brand"><span class="dot"></span>FELM Auction Group</div>
<a class="abs nav" style="left:383px">HOME</a>
<div class="abs nav-box" style="left:440px;width:143px">AUCTIONS<span class="caret"><svg width="8" height="5"><path d="M0 5L4 0L8 5z" fill="#fff"/></svg></span></div>
<div class="abs nav-box" style="left:602px;width:144px">SERVICES<span class="caret"><svg width="8" height="5"><path d="M0 0L4 5L8 0z" fill="#fff"/></svg></span></div>
<a class="abs nav" style="left:764px">ABOUT US</a>
<a class="abs nav" style="left:848px">REFERENCES</a>
<a class="abs nav" style="left:956px">FAQs</a>
<a class="abs nav" style="left:1006px">CONTACT</a>

<div class="abs hero" role="img" aria-label="Slideshow photo: white stucco house with tiled roof and an auction sign in front"></div>
<ul class="abs dropdown"><li>LIVE</li><li class="active">ONLINE</li><li>PAST</li></ul>

<div class="abs bar featured-bar">Featured Auctions</div>
<div class="abs arrow" style="left:113px">&lt;</div>
<div class="abs arrow" style="left:1059px">&gt;</div>

<div class="abs card" style="left:160px">
  <div class="photo" role="img" aria-label="Photo of a warehouse and office lot"></div>
  <h3>+/-103,000 Sq.Ft.<br>Factory/Warehouse/Office</h3>
  <div class="tag">LIVE ON-SITE AUCTION</div>
  <div class="meta"><b>Begins</b>Thursday, October 09, 2014<br>10:07 AM CDT</div>
  <div class="meta"><b>Location</b>3000 Marlow St.<br>Paducah, KY 42911</div>
  <span class="btn btn-red">Bid Online Now</span>
</div>
<div class="abs card" style="left:384px">
  <div class="photo" role="img" aria-label="Photo of a three bedroom house"></div>
  <h3>3 Bedroom House/ Vinyl<br>Sliding/Double Door Garage</h3>
  <div class="tag">LIVE ON-SITE AUCTION</div>
  <div class="meta"><b>Begins</b>Thursday, October 16, 2014<br>3:07 PM CDT</div>
  <div class="meta"><b>Location</b>1906 Fenn Street<br>Paducah, KY 42917</div>
  <span class="btn btn-red">Bid Online Now</span>
</div>
<div class="abs card" style="left:612px">
  <div class="photo" role="img" aria-label="Photo of a stone ranch home"></div>
  <h3>Pretty Bedford Stone Home<br>in Paducah, KY</h3>
  <div class="tag">LIVE ON-SITE AUCTION</div>
  <div class="meta"><b>Begins</b>Thursday, October 16, 2014<br>5:07 PM CDT</div>
  <div class="meta"><b>Location</b>1906 Fenn Street<br>Paducah, KY 42917</div>
  <span class="btn btn-red">Bid Online Now</span>
</div>
<div class="abs card" style="left:835px">
  <div class="photo" role="img" aria-label="Photo of a lake waterfront home"></div>
  <h3>+/-3,200 Sq.Ft. KY Lake<br>Waterfront Home</h3>
  <div class="tag">LIVE ON-SITE AUCTION</div>
  <div class="meta"><b>Begins</b>Thursday, October 16, 2014<br>5:07 PM CDT</div>
  <div class="meta"><b>Location</b>2401 Alder Street<br>Paducah, KY 42911</div>
  <span class="btn btn-red">Bid Online Now</span>
</div>

<div class="abs upcoming"></div>
<div class="abs bar upcoming-bar">Upcoming Auctions</div>

<div class="abs item" style="top:502px">
  <div class="thumb" role="img" aria-label="Aerial photo of a hunting farm"></div>
  <span class="ribbon">Featured</span>
  <h4>+/-64 ACRE GATED HUNTING FARM!!</h4>
  <p>Lorem ipsum dolor sit amet, consectetur adipisicing elit, sed do eiusmod tempor incididunt ut labore et dolore magna aliqua. Ut enim ad minim veniam, quis nostrud exercitation ullamco laboris nisi ut aliquip ex ea commodo consequat. Duis aute irure dolor in</p>
  <div class="row" style="top:66px"><svg viewBox="0 0 14 14"><circle cx="7" cy="7" r="7" fill="#e30613"/><path d="M7 3v4h3" stroke="#fff" stroke-width="1.5" fill="none"/></svg><span><b>Begins :</b> Thursday, October 23, 2014 at 10:07 AM CDT</span></div>
  <div class="row" style="top:81px"><svg viewBox="0 0 14 14"><circle cx="7" cy="7" r="7" fill="#e30613"/><path d="M7 3a2.5 2.5 0 0 1 2.5 2.5C9.5 7.5 7 11 7 11S4.5 7.5 4.5 5.5A2.5 2.5 0 0 1 7 3z" fill="#fff"/></svg><span><b>Location :</b> 1472 Birchwood Road, Salem, KY 42990</span></div>
  <div class="actions"><span class="btn btn-green">Add To Watchlist</span><span class="btn btn-red">Bid Online Now</span></div>
</div>
<div class="abs item" style="top:642px">
  <div class="thumb" role="img" aria-label="Aerial photo of a hunting farm"></div>
  <h4>+/-64 ACRE GATED HUNTING FARM!!</h4>
  <p>Lorem ipsum dolor sit amet, consectetur adipisicing elit, sed do eiusmod tempor incididunt ut labore et dolore magna aliqua. Ut enim ad minim veniam, quis nostrud exercitation ullamco laboris nisi ut aliquip ex ea commodo consequat. Duis aute irure dolor in</p>
  <div class="row" style="top:66px"><svg viewBox="0 0 14 14"><circle cx="7" cy="7" r="7" fill="#e30613"/><path d="M7 3v4h3" stroke="#fff" stroke-width="1.5" fill="none"/></svg><span><b>Begins :</b> Thursday, October 23, 2014 at 10:07 AM CDT</span></div>
  <div class="row" style="top:81px"><svg viewBox="0 0 14 14"><circle cx="7" cy="7" r="7" fill="#e30613"/><path d="M7 3a2.5 2.5 0 0 1 2.5 2.5C9.5 7.5 7 11 7 11S4.5 7.5 4.5 5.5A2.5 2.5 0 0 1 7 3z" fill="#fff"/></svg><span><b>Location :</b> 1472 Birchwood Road, Salem, KY 42990</span></div>
  <div class="actions"><span class="btn btn-green">Add To Watchlist</span><span class="btn btn-red">Bid Online Now</span></div>
</div>
<div class="abs item" style="top:782px">
  <div class="thumb" role="img" aria-label="Aerial photo of a hunting farm"></div>
  <h4>+/-64 ACRE GATED HUNTING FARM!!</h4>
  <p>Lorem ipsum dolor sit amet, consectetur adipisicing elit, sed do eiusmod tempor incididunt ut labore et dolore magna aliqua. Ut enim ad minim veniam, quis nostrud exercitation ullamco laboris nisi ut aliquip ex ea commodo consequat. Duis aute irure dolor in</p>
  <div class="row" style="top:66px"><svg viewBox="0 0 14 14"><circle cx="7" cy="7" r="7" fill="#e30613"/><path d="M7 3v4h3" stroke="#fff" stroke-width="1.5" fill="none"/></svg><span><b>Begins :</b> Thursday, October 23, 2014 at 10:07 AM CDT</span></div>
  <div class="row" style="top:81px"><svg viewBox="0 0 14 14"><circle cx="7" cy="7" r="7" fill="#e30613"/><path d="M7 3a2.5 2.5 0 0 1 2.5 2.5C9.5 7.5 7 11 7 11S4.5 7.5 4.5 5.5A2.5 2.5 0 0 1 7 3z" fill="#fff"/></svg><span><b>Location :</b> 1472 Birchwood Road, Salem, KY 42990</span></div>
  <div class="actions"><span class="btn btn-green">Add To Watchlist</span><span class="btn btn-red">Bid Online Now</span></div>
</div>
<a class="abs view-all">View All Auctions ---&gt;</a>

<section class="abs signup">
  <h2>Sign Up &amp; Get <em>FREE</em><br>Auction Alerts</h2>
  <hr>
  <div class="sms">SMS “SUB FAG” At :</div>
  <div class="num">1-800-555-BIDS (2437)</div>
  <div class="or">Or</div>
  <div class="lead">Fill your deatails below to get the latest news, articles and notifications about the auctions right into your inbox :</div>
  <div class="field" style="top:145px">Name :</div>
  <div class="field" style="top:168px">Email :</div>
  <div class="field" style="top:191px">Phone :</div>
  <div class="send">SEND</div>
</section>

<div class="abs bar video-bar">Latest Videos<span class="nav-arrows">&lt;&nbsp;&nbsp;&gt;</span></div>
<div class="abs video" role="img" aria-label="Video still: brick building with entrance stairs">
  <svg class="play" width="22" height="22" viewBox="0 0 22 22"><path d="M3 2L20 11L3 20z" fill="#e30613"/></svg>
</div>
<div class="abs video-title">Excellent Property for Investment</div>
<div class="abs video-text">Lorem ipsum dolor sit amet, consectetur adipisicing elit, sed do eiusmod tempor incididunt ut labore et dolore magna aliqua. Ut enim ad</div>
<div class="abs video-meta"><span>4 days ago</span><span><svg width="8" height="5"><ellipse cx="4" cy="2.5" rx="4" ry="2.5" fill="#e30613"/></svg>19 comments</span></div>

<div class="abs badges">
  <span class="badge" style="width:48px;height:30px"></span>
  <span class="badge" style="width:76px;height:28px;border-radius:50%"></span>
  <span class="badge" style="width:38px;height:30px;border-radius:50%"></span>
  <span class="badge" style="width:30px;height:32px"></span>
</div>

<footer class="abs footer"></footer>
<nav class="abs footer-nav"><a>Home</a><a>Auctions</a><a>Services</a><a>About Us</a><a>References</a><a>FAQs</a><a>Contact Us</a></nav>
<div class="abs footer-brand">FELM Auction<br>Group</div>
<address class="abs footer-contact">
  <b>FELM Auction Group</b><br>4172 Quill Ferry Lane, Paducah, KY 42917<br>1-800-555-BIDS (2437), Ph. (270) 555-0148<br>Fx. (270) 555-0193
</address>
<div class="abs legal" style="left:140px">Copyright © 2014 FELM Auction Group</div>
<div class="abs legal" style="left:838px">Privacy Policy</div>
<div class="abs legal" style="left:981px">Terms of Service</div>

</body>
</html>
```